Corvane Freight and Provision Service Brochure

Please see http://www.corvanefreight.example for who we are and what we do.
We would like to see a design that matches the industry we work in i.e. Oil and Gas. The design should communicate large, heavy field operations, supply of vast bulk fuel quantities to our US and Afghan Military customers, plus financial independence and the companies whatever it takes attitude operation in remote often hostile areas. Dark colors like on the website - contrasting our green logo. A strong focus on our past performance/past experience.

Target Market(s)

Military Customers, Partners, Subcontractors

Industry/Entity Type

Industry

Contact Information for Business Card

Display of Address, Phone, email etc. of our 4 offices

Font styles to use
Sans Serif

Requirements
Must have
• Glossy brochure, modern, cool design. Great display (map) of our offices in the Middle East, Europe and Central Asia. A focus on our past performance/past experience. Customer logos/references
Nice to have
• Prominent highlighted watermark logo
Should not have
• Standard A4/Letter brochure

```html
<!DOCTYPE html>
<html lang="en">
<head>
<meta charset="utf-8">
<title>Corvane Freight and Provision – Projects Spread</title>
<link href="https://fonts.googleapis.com/css2?family=Barlow:wght@400;500;600&family=Michroma&display=swap" rel="stylesheet">
<style>
  :root {
    --navy: #0d1e5c;
    --heading: #1d2a6b;
    --body: #3a3a3a;
    --green: #8ee61c;
    --frame: #9a9a9a;
    --paper: #ffffff;
  }
  * { margin: 0; padding: 0; box-sizing: border-box; }
  html, body { width: 1200px; height: 1000px; overflow: hidden; background: var(--paper); }
  body { position: relative; font-family: "Barlow", Arial, sans-serif; }
  .page { position: absolute; top: 288px; height: 425px; width: 600px; border: 1px solid var(--frame); overflow: hidden; background: var(--paper); }
  .page--left { left: 0; }
  .page--right { left: 600px; border-left: none; }
  .photo { position: absolute; }
  .photo--refuel { left: 0; top: 0; width: 600px; height: 425px;
    background: linear-gradient(180deg, #e9ecef 0%, #d2d6da 22%, #7d858c 45%, #4b5259 70%, #2e3338 100%); }
  .photo-fade { position: absolute; left: 395px; top: 0; width: 205px; height: 425px; background: rgba(255,255,255,0.78); }
  .photo--nozzle { left: 418px; top: 0; width: 142px; height: 106px; background: linear-gradient(135deg, #c9c3b6, #6f6656 55%, #3a332b); }
  .photo--flag { left: 38px; top: 0; width: 161px; height: 106px; background: radial-gradient(circle at 60% 45%, #4f8a3a 0%, #8a1a1a 25%, #12204a 55%, #0a1130 100%); }
  .photo--road { left: 220px; top: 0; width: 160px; height: 106px; background: linear-gradient(180deg, #8eaac9 0%, #c7a67c 35%, #9a7d55 65%, #5a5a56 100%); }
  .photo--trucks { left: 400px; top: 0; width: 160px; height: 106px; border: 2px solid #111; background: linear-gradient(160deg, #4b6a3e, #8a8f8c 50%, #2e3a2a); }
  .section-band { position: absolute; left: 0; top: 115px; width: 418px; height: 56px; background: var(--navy); color: #fff; padding: 13px 0 0 58px; }
  .section-band__title { font-family: "Michroma", "Barlow", sans-serif; font-size: 12px; letter-spacing: 0.5px; line-height: 14px; }
  .section-band__sub { font-size: 10px; letter-spacing: 0.6px; margin-top: 2px; font-weight: 400; }
  .project { position: absolute; top: 126px; width: 162px; }
  .project__title { color: var(--heading); font-weight: 500; font-size: 9.6px; line-height: 11.5px; margin-bottom: 4px; }
  .project__text { color: var(--body); font-size: 6.9px; line-height: 9.3px; margin-bottom: 3px; }
  .page--left .project { left: 418px; width: 142px; }
  .page--left .project__text { color: #444; }
  .col-1 { left: 38px; }
  .col-2 { left: 220px; }
  .col-3 { left: 400px; }
  .folio { position: absolute; top: 394px; width: 20px; height: 30px; background: var(--green); color: #fff; font-size: 6px; text-align: center; line-height: 30px; }
  .page--left .folio { left: 540px; }
  .page--right .folio { left: 540px; }
  .page-label { position: absolute; top: 772px; font-size: 24px; font-family: Arial, sans-serif; color: #000; }
</style>
</head>
<body>
  <section class="page page--left">
    <div class="photo photo--refuel" role="img" aria-label="Aircraft being refuelled on the apron by a worker in a high-visibility vest beside a fuel truck"></div>
    <div class="photo-fade"></div>
    <div class="photo photo--nozzle" role="img" aria-label="Gloved hand holding an aviation fuel nozzle"></div>
    <div class="section-band">
      <div class="section-band__title">WHO WE ARE</div>
      <div class="section-band__sub">FEW OF OUR PRESTIGIOUS PROJECTS</div>
    </div>
    <article class="project">
      <h2 class="project__title">MoD - AAF Aviation Fuel Supply Contract - Contract Number W56KJD-14-D-0011</h2>
      <p class="project__text">We are an incumbent contractor for this requirement of the Ministry of Defence of Afghanistan and we have performed our duties exceptionally well.</p>
      <p class="project__text">This contract is the primary support mechanism for Afghan Air Force (AAF) requirements throughout Afghanistan and for all Direct-Into-Plane (Into-Aircraft) fuel requirements of the AAF.</p>
      <p class="project__text">Corvane fulfills the Government requirements according to terms established in the basic contract and resulting delivery orders. We accomplish all required commodity sourcing and transportation services to delivery points specified in resulting requests for service on a on a free on board (F.O.B.) Destination basis.</p>
    </article>
    <div class="folio">10</div>
  </section>

  <section class="page page--right">
    <div class="photo photo--flag" role="img" aria-label="Afghan flag held aloft against a dark blue sky"></div>
    <div class="photo photo--road" role="img" aria-label="Desert road through dry mountains"></div>
    <div class="photo photo--trucks" role="img" aria-label="Convoy of heavy trucks on a mountain road"></div>

    <article class="project col-1">
      <h2 class="project__title">Bulk Diesel Supply To Kandahar Power Plants - Contract Number W56KJD-15-C-0002</h2>
      <p class="project__text">The contract is a primary support mechanism for fuel requirements of the NRPA Kandahar Bridging Solution (KBS) power generation. It provides fuel for the operation of the two (2) diesel power plants built under the KBS program which are located at Shurandam Industrial Park (SIP) and Bagh-e-Pol (BEP). The fuel will allow electrical power generation for Kandahar City while the Northeast Power System (NEPS) – Southeast Power Systems (SEPS) connector is being completed.</p>
      <p class="project__text">Corvane accomplishes all required commodity sourcing and delivery to points specified in the contract on a free on board (F.O.B.) Destination basis. Corvane is responsible for a performance-based contracting relationship, where its customer the US-Government specifies the desired end-state and Corvane executes an effective ‘turn-key’ sourcing solution for required commodities and all transportation to the specified delivery locations.</p>
    </article>

    <article class="project col-2">
      <h2 class="project__title">Afghan Transportation Network (ATN) – South – Contract Number HTC711-14-D-R061</h2>
      <p class="project__text">The Afghanistan Transportation Network (ATN) uses a network of U.S. Government (USG) approved Afghan privately owned trucking companies, otherwise known as Elder Owned Companies (EOCs) or locally-owned and locally-operated subcontractors. Corvane manages the approved EOCs or approved subcontractors to provide secure, reliable cargo and fuel transportation services to and from locations in the provinces of Day Kundi, Uruzgan, Zabul, and Kandahar of Afghanistan without the use of convoy security.</p>
      <p class="project__text">The use of ATN regional transportation companies capitalizes on existing business agreements to promote the development of new business agreements with influential regional leaders. This capitalization of existing business agreements into new areas and companies allows Afghan infrastructure to develop, implement and sustain an Afghan-owned and operated transportation network capable of providing secure and reliable</p>
    </article>

    <article class="project col-3">
      <h2 class="project__title">National Afghan Trucking II – Contract Number HTC711-14-D-R049</h2>
      <p class="project__text">The principal contract supporting the U.S. supply chain in Afghanistan is called National Afghan Trucking (NAT). Although there are other supply chain contracts, the NAT contracts provides trucking for over 70 percent of the total goods and material distributed to U.S. troops in the field. The trucks carry fuel, food, supplies, and heavy equipment. Corvane provides all management and logistics support resources necessary to pick-up cargo (material or equipment) at origin and delivers cargo to destination on Required Delivery Date (RDD) established by its customer.</p>
      <p class="project__text">Corvane is constantly rated as one of the top carriers under this contract that is governed by the strict confines of a by the customer fully developed QA program detailed in an associated Quality Assurance Surveillance Plan (QASP) document that defines how performance standards will be applied; frequency of surveillance; and minimum acceptable defect rate(s).</p>
    </article>
    <div class="folio">11</div>
  </section>

  <div class="page-label" style="left:323px;">Page 10</div>
  <div class="page-label" style="left:860px;">Page 11</div>
</body>
</html>
```